Need a flyer to leave behind when visiting clients or at shows

Glossy colorful tri-fold flyer with the same information that is on my web site www.brevalinkpro.com. I am open to a little modern or creative take on the typical brochure. I created the web site so I can provide any raw files needed from it. I would also like the ability to edit this flyer in the future in Adobe Photoshop Elements

```html
<!DOCTYPE html>
<html lang="en">
<head>
<meta charset="utf-8">
<title>BrevaLink Tri-Fold Brochure</title>
<link href="https://fonts.googleapis.com/css2?family=Montserrat:wght@500;600;700&family=Open+Sans:wght@400;600&display=swap" rel="stylesheet">
<style>
  :root {
    --purple: #6b2fa0;
    --purple-dark: #4c1f76;
    --purple-light: #9a6cc8;
    --lilac: #e9dff3;
    --ink: #3a3340;
    --muted: #6d6675;
    --paper: #ffffff;
    --stage: #d8d8da;
  }
  * { box-sizing: border-box; margin: 0; padding: 0; }
  html, body { width: 1200px; height: 2400px; overflow: hidden; }
  body { background: var(--stage); font-family: "Open Sans", sans-serif; color: var(--ink); position: relative; }

  .spread {
    position: absolute; left: 50px; width: 1100px; height: 850px;
    display: grid; grid-template-columns: repeat(3, 1fr);
    background: var(--paper); box-shadow: 0 14px 40px rgba(0,0,0,.22);
  }
  .spread--outside { top: 230px; }
  .spread--inside { top: 1320px; }
  .panel { position: relative; overflow: hidden; border-right: 1px solid #eee; }
  .panel:last-child { border-right: none; }

  .heading { display: flex; align-items: center; gap: 12px; font-family: "Montserrat", sans-serif; font-weight: 700; color: var(--purple); font-size: 24px; margin-bottom: 16px; }
  .heading__icon { width: 30px; height: 30px; background: var(--purple); border-radius: 4px; flex: none; }
  .subheading { font-family: "Montserrat", sans-serif; font-weight: 600; color: var(--purple); font-size: 19px; margin: 26px 0 8px; }
  .body-text { font-size: 15px; line-height: 1.6; color: var(--muted); margin-bottom: 12px; }

  /* Outside */
  .leadership__text { padding: 46px 36px 0; height: 520px; }
  .leadership__band { position: absolute; left: 0; bottom: 0; width: 100%; height: 330px; background: var(--purple); padding: 40px 36px; display: flex; gap: 20px; align-items: flex-start; }
  .portrait { width: 150px; height: 180px; background: linear-gradient(160deg, #b8bcc4, #5d6270); flex: none; }
  .leadership__caption { color: var(--paper); padding-top: 110px; }
  .leadership__name { font-family: "Montserrat", sans-serif; font-weight: 700; font-size: 17px; }
  .leadership__role { font-size: 13px; opacity: .85; margin-top: 4px; }

  .cover-photo { position: absolute; top: 0; left: 366.67px; width: 733.33px; height: 520px; background: linear-gradient(135deg, #f3e9e2 0%, #e6d7d0 45%, #c9b2c9 100%); }
  .outside-band { position: absolute; bottom: 0; left: 366.67px; width: 733.33px; height: 330px; background: var(--purple); }
  .contact { position: absolute; left: 0; top: 0; width: 366.67px; height: 100%; padding: 70px 36px; display: flex; flex-direction: column; gap: 26px; color: var(--paper); font-size: 15px; }
  .contact__row { display: flex; align-items: center; gap: 14px; }
  .contact__icon { width: 34px; height: 34px; border-radius: 50%; background: var(--paper); flex: none; display: flex; align-items: center; justify-content: center; }
  .cover-brand { position: absolute; right: 0; top: 0; width: 366.67px; height: 100%; padding: 60px 36px; color: var(--paper); }
  .brand-name { display: flex; align-items: center; gap: 12px; font-family: "Montserrat", sans-serif; font-weight: 700; font-size: 38px; color: var(--paper); }
  .brand-name__mark { width: 22px; height: 22px; background: var(--paper); }
  .tagline { font-family: "Montserrat", sans-serif; font-weight: 700; font-size: 23px; line-height: 1.3; margin-top: 34px; }

  /* Inside */
  .inside-panel { padding: 46px 36px; }
  .bullet-list { list-style: none; }
  .bullet-list li { position: relative; padding-left: 22px; font-size: 15px; line-height: 1.5; color: var(--muted); margin-bottom: 12px; }
  .bullet-list li::before { content: ""; position: absolute; left: 0; top: 8px; width: 9px; height: 9px; background: var(--purple); }
  .hex-art { position: absolute; left: 0; bottom: 0; width: 100%; height: 270px; background: linear-gradient(180deg, #ffffff 0%, var(--lilac) 30%, var(--purple-light) 70%, var(--purple-dark) 100%); }
  .values-list { list-style: none; }
  .values-list li { display: flex; align-items: center; gap: 14px; font-family: "Montserrat", sans-serif; font-weight: 600; font-size: 17px; color: var(--ink); padding: 12px 0; border-bottom: 1px solid var(--lilac); }
  .values-list li::before { content: ""; width: 14px; height: 14px; border-radius: 50%; background: var(--purple); flex: none; }

  .services__band { height: 130px; background: var(--purple); padding: 46px 36px; }
  .services__band .heading { color: var(--paper); }
  .services__band .heading__icon { background: var(--paper); }
  .services__body { padding: 28px 36px; }
  .services-photo { position: absolute; left: 0; bottom: 0; width: 100%; height: 260px; background: linear-gradient(135deg, #2a4d7a 0%, #5b88b8 55%, #c7d9ea 100%); }
</style>
</head>
<body>

<section class="spread spread--outside">
  <div class="panel leadership">
    <div class="leadership__text">
      <h2 class="heading"><span class="heading__icon"></span>Leadership Team</h2>
      <p class="body-text">Our founder brings twenty years of hands-on experience helping small and mid-sized firms plan, secure and support their technology.</p>
      <p class="body-text">Every client works directly with a certified engineer who knows their network.</p>
    </div>
    <div class="leadership__band">
      <div class="portrait" role="img" aria-label="Portrait photograph of the company founder"></div>
      <div class="leadership__caption">
        <p class="leadership__name">Daniel Mercer</p>
        <p class="leadership__role">Founder &amp; Principal Engineer</p>
      </div>
    </div>
  </div>
  <div class="panel"></div>
  <div class="panel"></div>

  <div class="cover-photo" role="img" aria-label="Photograph of hands working on a laptop at a bright desk"></div>
  <div class="outside-band">
    <div class="contact">
      <div class="contact__row">
        <span class="contact__icon"><svg width="18" height="18" viewBox="0 0 24 24"><path d="M6.6 10.8a15 15 0 0 0 6.6 6.6l2.2-2.2a1 1 0 0 1 1-.25 11.4 11.4 0 0 0 3.6.57 1 1 0 0 1 1 1V20a1 1 0 0 1-1 1A17 17 0 0 1 3 4a1 1 0 0 1 1-1h3.5a1 1 0 0 1 1 1c0 1.25.2 2.45.57 3.57a1 1 0 0 1-.25 1z" fill="#6b2fa0"/></svg></span>
        (555) 014-2280
      </div>
      <div class="contact__row">
        <span class="contact__icon"><svg width="18" height="18" viewBox="0 0 24 24"><rect x="3" y="5" width="18" height="14" rx="2" fill="none" stroke="#6b2fa0" stroke-width="2"/><path d="M3 7l9 6 9-6" fill="none" stroke="#6b2fa0" stroke-width="2"/></svg></span>
        info@brevalinkpro.com
      </div>
      <div class="contact__row">
        <span class="contact__icon"><svg width="18" height="18" viewBox="0 0 24 24"><circle cx="12" cy="12" r="9" fill="none" stroke="#6b2fa0" stroke-width="2"/><path d="M3 12h18M12 3c3 3 3 15 0 18M12 3c-3 3-3 15 0 18" fill="none" stroke="#6b2fa0" stroke-width="1.6"/></svg></span>
        www.brevalinkpro.com
      </div>
    </div>
    <div class="cover-brand">
      <div class="brand-name"><span class="brand-name__mark"></span>BrevaLink</div>
      <p class="tagline">Increasing The Value and Security of Your Technology Resources</p>
    </div>
  </div>
</section>

<section class="spread spread--inside">
  <div class="panel inside-panel">
    <h2 class="heading"><span class="heading__icon"></span>Primary Objective</h2>
    <ul class="bullet-list">
      <li>Understand and secure client technology</li>
      <li>Committed to a proactive approach</li>
      <li>Provide reliable, cost-effective support</li>
    </ul>
    <h3 class="subheading">Our Mission</h3>
    <p class="body-text">Deliver dependable IT service that lets clients focus on business.</p>
    <div class="hex-art" role="img" aria-label="Purple hexagon graphic rising from the bottom of the panel"></div>
  </div>

  <div class="panel inside-panel">
    <h2 class="heading"><span class="heading__icon"></span>Core Values</h2>
    <ul class="values-list">
      <li>Commitment</li>
      <li>Innovation</li>
      <li>Integrity</li>
      <li>Professional Development</li>
    </ul>
    <h3 class="subheading">Our Vision</h3>
    <p class="body-text">To be the trusted technology partner for every client we serve.</p>
    <h3 class="subheading">Our Goal</h3>
    <p class="body-text">Long-term relationships built on honest advice and quick response.</p>
  </div>

  <div class="panel services">
    <div class="services__band">
      <h2 class="heading"><span class="heading__icon"></span>Services</h2>
    </div>
    <div class="services__body">
      <p class="body-text">Complete solutions for homes and businesses.</p>
      <h3 class="subheading">Technology Consulting</h3>
      <ul class="bullet-list">
        <li>Network Design</li>
        <li>Managed Security</li>
        <li>Cloud Backup</li>
        <li>Help Desk Support</li>
      </ul>
    </div>
    <div class="services-photo" role="img" aria-label="Photograph of a hand touching a glowing technology interface"></div>
  </div>
</section>

</body>
</html>
```